Veltrano Community Development Planning New web site

Design a new web site. I have a budget of $1,500.00.
Attached on PowerPoint is a complete site plan. Home page and linked pages.
10 - 12 pages. All copy and photos will be supplied. (300dpi)
I have shown them the concept which they like.
No data bases required. Home page with animations dissolving.
They former web site has been taken down. They have been in business 30 years in New Jersey
Colors teal blues and greens
There will be a new logo)being designed)
The text in home page copy will give you a detailed story what they are all about.

files have been approved for Veltrano, Inc.   Tomas is the designer

Industry/Entity Type

Community

```html
<!DOCTYPE html>
<html lang="en">
<head>
<meta charset="utf-8">
<title>Veltrano Community Development Planning</title>
<link href="https://fonts.googleapis.com/css2?family=Roboto:wght@300;400;500;700&display=swap" rel="stylesheet">
<style>
:root{
  --green:#2fb56b;
  --green-text:#34b36b;
  --yellow:#f4e31a;
  --ink:#1b1b1b;
  --body:#444;
  --light:#f3f3f3;
  --dark:#4a4a4a;
  --footer:#111;
}
*{margin:0;padding:0;box-sizing:border-box}
html,body{width:730px;height:1200px;overflow:hidden;background:#fff}
body{font-family:'Roboto',Arial,sans-serif;color:var(--body);position:relative}
.abs{position:absolute}

.site-header{position:absolute;left:0;top:0;width:730px;height:75px;border-bottom:2px solid var(--green);background:#fff}
.brand{left:75px;top:22px;font-size:29px;font-weight:700;color:var(--ink);letter-spacing:-0.5px}
.phones{right:72px;top:10px;display:flex;gap:14px;align-items:center}
.phone{display:flex;align-items:center;gap:6px;color:var(--green-text);font-weight:700;font-size:13px}
.phone + .phone{border-left:1px solid #ccc;padding-left:12px}
.main-nav{left:242px;top:50px;display:flex;font-size:9.5px;color:#222}
.main-nav a{color:inherit;text-decoration:none;padding:7px 8px;height:24px;display:block}
.main-nav a.active{background:var(--green);color:#fff}
.main-nav a + a{border-left:1px dotted #aaa;margin-left:4px}

.hero{top:77px;left:0;width:730px;height:303px;background:#f2f2f2}
.hero-photo{position:absolute;left:300px;top:0;width:430px;height:303px;background:linear-gradient(90deg,#f2f2f2 0%,#dfe6ee 30%,#b9cbe0 70%,#a9bfd8 100%)}
.hero-title{left:72px;top:93px;font-size:33px;font-weight:700;color:var(--ink);letter-spacing:-0.5px}
.hero-sub{left:74px;top:136px;font-size:12px;color:var(--green-text);width:230px;line-height:13px}

.services{top:403px;left:73px;display:flex;gap:3px}
.tile{width:144px;height:97px;border-bottom:3px solid var(--yellow);color:#fff;text-align:center;display:flex;flex-direction:column;justify-content:flex-start;padding-top:20px;font-weight:500;font-size:14px;line-height:14.5px}
.tile small{font-size:8px;line-height:10px;font-weight:500}
.t1{background:linear-gradient(#3f5a35,#2d3a28)}
.t2{background:linear-gradient(#5a5048,#2e2a27)}
.t3{background:linear-gradient(#5b5b5b,#333)}
.t4{background:linear-gradient(#3a3a3a,#1f1f1f)}

.about{top:523px;left:0;width:730px;height:320px;background:var(--light)}
.heading{font-size:19px;font-weight:500;color:var(--ink);padding-bottom:2px;border-bottom:4px solid var(--green);display:inline-block}
.col-left{left:72px;top:551px;width:288px;font-size:9.4px;line-height:12px}
.col-left p{margin-top:8px}
.col-left .heading + p{margin-top:22px}
.divider{left:366px;top:577px;width:0;height:222px;border-left:1px dotted #999}
.col-right{left:394px;top:549px;width:280px;font-size:9.4px;line-height:12px}
.col-right .heading{font-size:19px;text-transform:uppercase}
.results{list-style:none;margin-top:22px}
.results li{position:relative;padding-left:12px;margin-bottom:5px}
.results li::before{content:"";position:absolute;left:0;top:3px;width:5px;height:5px;background:var(--yellow)}
.results a{color:var(--green-text)}
.note{font-size:7.2px;line-height:11px;margin-top:14px}
.note b{color:var(--green-text)}
.note .big{font-size:10px}
.contact-line{font-size:8px;color:var(--ink)}
.contact-line .g{color:var(--green-text)}

.members-band{top:843px;left:0;width:730px;height:55px;background:var(--green);color:#fff;text-align:center;font-size:30px;font-weight:500;line-height:55px}
.members{top:898px;left:0;width:730px;height:210px;background:linear-gradient(#555,#3c3c3c)}
.members-notch{left:357px;top:890px}
.member-list{top:48px;left:0;width:730px;text-align:center;font-size:25px;line-height:31px;letter-spacing:-0.3px}
.member-list .hl{color:var(--yellow);font-weight:500}
.member-list .plain{color:#fff;font-weight:300}

.site-footer{top:1108px;left:0;width:730px;height:92px;background:var(--footer)}
.foot-nav{left:66px;top:27px;display:flex;font-size:8px;color:#aaa}
.foot-nav span{padding:0 10px}
.foot-nav span + span{border-left:1px dotted #666}
.foot-brand{right:80px;top:17px;font-size:23px;font-weight:700;color:#555}
.foot-rule{left:0;top:67px;width:730px;border-top:1px solid #2a2a2a}
.copyright{left:0;top:78px;width:730px;text-align:center;font-size:7px;color:#888}
.copyright b{color:#bbb;font-weight:500}
</style>
</head>
<body>

<header class="site-header">
  <div class="abs brand">Veltrano</div>
  <div class="abs phones">
    <div class="phone">
      <svg width="18" height="18" viewBox="0 0 24 24"><path d="M6 3l3 4-2 2c1 3 4 6 7 7l2-2 4 3-2 3C10 20 4 14 3 6z" fill="#222"/><circle cx="17" cy="6" r="5" fill="#f4c21a"/></svg>
      (555) 214-3860
    </div>
    <div class="phone">
      <svg width="18" height="18" viewBox="0 0 24 24"><rect x="3" y="6" width="18" height="16" rx="2" fill="#222"/><rect x="6" y="2" width="8" height="6" fill="#222"/><rect x="6" y="11" width="12" height="2" fill="#f4c21a"/><rect x="6" y="15" width="12" height="2" fill="#f4c21a"/></svg>
      (555) 214-3871
    </div>
  </div>
  <nav class="abs main-nav">
    <a class="active" href="#">Home</a>
    <a href="#">Our Company</a>
    <a href="#">Housing Rehab Application</a>
    <a href="#">Affordable Application</a>
    <a href="#">Contact Us</a>
  </nav>
</header>

<section class="abs hero">
  <div class="hero-photo" role="img" aria-label="Photo of a businessman drawing a business plan diagram on glass"></div>
  <h1 class="abs hero-title" style="top:93px">Ipsum dolor sit</h1>
  <p class="abs hero-sub">Lorem ipsum dolor sit amet, consectetuer adipiscing elit,</p>
</section>

<section class="abs services">
  <div class="tile t1" role="img" aria-label="Community development photo">Community<br>Development<br>Planning</div>
  <div class="tile t2" role="img" aria-label="Paperwork signing photo">Housing<br>Rehabilitation<br>Administration</div>
  <div class="tile t3" role="img" aria-label="Government building photo">US Department of<br>Housing and Urban<br>Development<small>(HUD)<br>Program Management</small></div>
  <div class="tile t4" role="img" aria-label="Dark architectural photo"><span style="font-size:16px;line-height:19px">Implementation<br>of Programs</span><small>under the Jurisdiction of<br>New Jersey Council of<br>Affordable Housing (COAH)</small></div>
</section>

<section class="abs about"></section>
<article class="abs col-left">
  <h2 class="heading">Veltrano, Inc</h2>
  <p>Is a city planning firm that specializes in community development and housing rehabilitation program planning, design and implementation. We have over twenty years of experience in developing and administering income base-base housing and programs in accordance with US Department of Housing and Urban Development (HUD) and New Jersey Council on Affordable Housing (COAH) rules and regulations,</p>
  <p>In addition, our firm is capable of providing the technical and administrative assistance our clients require for implementation of their income based housing programs. Marlow Hale Associates is one of the most experience urban planning firms in New Jersey, with over forty years of as consulting planners.</p>
  <p class="note" style="margin-top:20px">To find out more about federal housing programs that we will administer,<br><b>please go to <span class="big">www.housing-programs.example</span></b></p>
</article>
<div class="abs divider"></div>
<article class="abs col-right">
  <h2 class="heading">We get results</h2>
  <ul class="results">
    <li>Veltrano designs income based programs to be supported by federal placement lotteries state funding</li>
    <li>We implement local programs to benefit people seeking access to affordable housing.</li>
    <li>Our experienced staff screen applicants for local affordable housing</li>
    <li>We pre-qualify persons who have applied for housing rehabilitation.<br><a href="#">Conduct placement lotteries</a></li>
    <li>Through local housing rehabilitation programs, our experience construction inspectors determine what improvements are required at eligible units based on local building codes and health and safety issues</li>
  </ul>
  <p class="note" style="margin-top:12px;margin-left:-6px">For more information about out services, please contact us today at<br>
  <span class="contact-line">VELTRANO <span class="g">(555) 214-3860</span> or <span class="g">office@veltrano.example</span></span></p>
</article>

<div class="abs members-band">MEMBERSHIPS</div>
<section class="abs members" role="img" aria-label="Faded city skyline photo behind membership list">
  <div class="abs member-list">
    <div class="hl">National Neighborhood Renewal Alliance</div>
    <div class="hl">Garden State Planning Guild</div>
    <div class="plain">Coastal Planning Officials Forum Regional</div>
    <div class="plain">Community Housing Network</div>
  </div>
</section>
<svg class="abs members-notch" width="16" height="9" viewBox="0 0 16 9"><path d="M0 0h16L8 9z" fill="#2fb56b"/></svg>

<footer class="abs site-footer">
  <nav class="abs foot-nav">
    <span>Home</span><span>Our Company</span><span>Housing Rehab Application</span><span>Affordable Application</span><span>Contact Us</span>
  </nav>
  <div class="abs foot-brand">Veltrano</div>
  <div class="abs foot-rule"></div>
  <p class="abs copyright">Copy Right 2014 Veltrano, 218 Harbor View Lane, Cedar Point, New Jersey, 08000 &nbsp; <b>TEL (555) 214-3860 Fax (555) 214-3871</b></p>
</footer>

</body>
</html>
```